Website design for headhunting agency

The design I need (PSD file) is for a company offering specialised services in recruitment of high-end executive and management positions for businesses.
OBJECTIVES OF THE WEBSITE:
1. Let entrepreneurs and business leaders know about their services and easily have them contact Varolinq if they want more information about their services.
2. Display a list of available carreer opportunities (according to their client's need).
WHAT I NEED:
1st, I need the design for the Home Page ONLY. Once approved, I will need the other pages designed as well. (Here is prototype that we've already developed for the Website that will guide you in the design:
http://demo.pelvarshop.net/varolinq/fr/accueil)
ATTACHED FILES
- Logo
- PDF brochure: Use for inspiration. It is encouraged that you use pictures from this brochure. You can always suggest new ones, as long as they are not expensive to buy and have the same look and feel as the brochure.
HOMEPAGE:
1. Main menu : 6 sections
Accueil | Varolinq | Équipe | Approche | Postes disponibles | Publications
2. Main slider: 4 sections
- Chasseurs de têtes (Headhunters)
- Notre approche (Our Approach)
- Postes cadres disponibles (Executive Careers
Opportunities)
- Contactez-nous (Contact Us)
3. Main Call To Action Boxes :
- Liste Des postes disponibles (Liste of Available Careers
Opportunities)
- Formulaire de contact (contact form)
4. Latest blog articles
- Les derniers articles.
OTHER PAGES (to design once Homepage is approved)
- Varolinq (about us)
- Équipe (our team)
- Approche (our approach)
- Postes disponibles (Career opportunities)
- Publications (blog articles)
- Contact (Contact us)
Target Market(s)
ORGANIZATIONS:
Leaders of organizations seeking to recruit highly qualified staff.
HIGHLY QUALIFIED RESOURCES:
Senior individuals seeking a salary between $70,000 and $ $200,000 annually
PROFESSIONAL SECTORS:
manufacturing : Primary and secondary industries
pharmaceutical
Aerospace
Finances
Retail business
Engineering
Chemical and petrochemical
IT, telecommunications and high technology
Professional Organizations and Association
Industry/Entity Type
Business
Look and feel
Each slider illustrates characteristics of the customer's brand and the style your logo design should communicate.

```html
<!DOCTYPE html>
<html lang="fr">
<head>
<meta charset="utf-8">
<title>Varolinq – Recherche de cadres</title>
<link rel="stylesheet" href="https://fonts.googleapis.com/css2?family=Montserrat:wght@400;600;700&family=Arimo:wght@400;700&display=swap">
<style>
:root{
  --teal:#0d4a55;
  --teal-dark:#093a43;
  --teal-deep:#072f36;
  --orange:#e8a51b;
  --nav-bg:#e5e7e8;
  --careers-bg:#c5cdd1;
  --btn-grey:#5b7e87;
  --text:#3d4a4f;
  --muted:#7d8a8f;
  --white:#ffffff;
}
*{box-sizing:border-box;margin:0;padding:0}
html,body{width:984px;height:1200px;overflow:hidden}
body{font-family:"Arimo",Arial,sans-serif;color:var(--text);background:var(--white);position:relative}
.page{position:relative;width:984px;height:1200px;overflow:hidden}
.abs{position:absolute}
.heading{font-family:"Montserrat",Arial,sans-serif;font-weight:700;color:var(--teal);text-transform:uppercase}

/* header */
.top-line{left:0;top:0;width:984px;height:4px;background:var(--orange)}
.util-nav{right:118px;top:15px;display:flex;gap:0;font-family:"Montserrat",sans-serif;font-size:10px;font-weight:600;color:var(--teal-deep)}
.util-nav span{padding:0 10px;border-left:1px solid #999;line-height:11px}
.util-nav span:first-child{border-left:none}
.main-bar{left:0;top:36px;width:984px;height:54px;background:var(--nav-bg);border-top:1px solid #d3d6d8}
.logo-box{left:115px;top:4px;width:227px;height:86px;background:var(--white);text-align:center}
.logo-mark{position:absolute;left:105px;top:6px;width:16px;height:16px;background:var(--teal)}
.logo-name{position:absolute;left:0;top:32px;width:100%;font-family:"Montserrat",sans-serif;font-weight:600;font-size:30px;color:var(--teal);letter-spacing:1px}
.logo-tag{position:absolute;left:0;top:68px;width:100%;font-size:12px;color:var(--teal)}
.main-nav{left:344px;top:36px;height:54px;display:flex}
.main-nav a{display:block;height:54px;line-height:50px;padding:0 10px;font-family:"Montserrat",sans-serif;font-weight:700;font-size:12px;color:var(--teal);text-decoration:none;border-right:1px solid #cfd3d5}
.main-nav a.active{color:var(--orange);border-top:3px solid var(--orange);line-height:46px;background:#eceeef}

/* hero */
.hero{left:0;top:90px;width:984px;height:314px;background:#e9eff0}
.hero-photo{left:0;top:0;width:540px;height:314px;background:linear-gradient(120deg,#c9d6da 0%,#e8eef0 45%,#d4e0e3 100%)}
.hero-title{left:552px;top:40px;font-size:19px;line-height:25px;letter-spacing:.3px}
.hero-text{left:554px;top:98px;width:270px;font-size:12px;line-height:21px;color:var(--teal-deep)}
.hero-btn{left:553px;top:212px;width:267px;height:50px;background:var(--teal);border-bottom:3px solid var(--orange);color:var(--white);font-family:"Montserrat",sans-serif;font-weight:700;font-size:17px;line-height:47px;padding-left:30px}
.hero-btn svg{position:absolute;right:30px;top:16px}
.slide-arrow{top:130px;width:38px;height:38px;border-radius:50%;background:rgba(255,255,255,.55)}
.slide-arrow svg{position:absolute;left:13px;top:11px}

/* careers */
.careers{left:0;top:404px;width:984px;height:332px;background:var(--careers-bg)}
.careers-title{left:0;top:14px;width:984px;text-align:center;font-size:19px;letter-spacing:.5px}
.careers-rule{left:250px;top:46px;width:484px;height:1px;background:#8fa3a9}
.careers-notch{left:485px;top:46px}
.career{top:80px;width:200px}
.career-icon{position:absolute;left:0;top:0;width:42px;height:42px;border-radius:50%;border:3px solid var(--teal);background:var(--white)}
.career-icon svg{position:absolute;left:8px;top:7px}
.career h3{position:absolute;left:66px;top:8px;white-space:nowrap;font-size:15px}
.career p{position:absolute;left:66px;top:34px;width:180px;font-size:12px;line-height:18px;color:#55666b}
.apply-btn{position:absolute;left:66px;top:93px;width:128px;height:30px;background:var(--btn-grey);color:var(--white);font-family:"Montserrat",sans-serif;font-weight:700;font-size:10px;line-height:30px;padding-left:13px;box-shadow:0 1px 2px rgba(0,0,0,.25)}
.apply-btn svg{position:absolute;right:20px;top:11px}

/* quick form */
.quick{left:116px;top:644px;width:750px;height:75px;background:var(--teal);border:3px solid var(--white);box-shadow:0 1px 3px rgba(0,0,0,.2)}
.quick-label{left:18px;top:24px;font-family:"Montserrat",sans-serif;font-weight:700;font-size:18px;color:var(--orange)}
.quick-arrow{left:208px;top:-3px}
.field{background:var(--teal-dark);border:1px solid #0f5966;color:#9fb3b8;font-size:10px;padding:8px}
.f-name{left:249px;top:6px;width:157px;height:28px}
.f-mail{left:249px;top:38px;width:157px;height:28px}
.f-msg{left:412px;top:6px;width:156px;height:60px}
.submit{left:584px;top:10px;width:118px;height:46px;background:var(--orange);color:var(--white);font-family:"Montserrat",sans-serif;font-weight:700;font-size:17px;line-height:46px;text-align:center;box-shadow:0 2px 0 #c48812}

/* blog */
.col-head{font-size:15px;padding-bottom:7px;border-bottom:5px solid #e4e6e7}
.blog-head{left:116px;top:770px;width:366px}
.date{left:118px;top:811px;width:46px;height:42px;background:var(--teal);color:var(--white);text-align:center;font-family:"Montserrat",sans-serif;font-weight:700}
.date b{display:block;font-size:20px;line-height:24px}
.date i{display:block;font-style:normal;font-size:11px;line-height:12px;background:var(--white);color:var(--teal);margin:0 3px;border-top:2px solid var(--white)}
.date-month{position:absolute;left:0;top:26px;width:46px;font-size:11px}
.post-title{left:175px;top:810px;font-family:"Montserrat",sans-serif;font-size:19px;color:var(--teal);line-height:22px}
.post-sub{left:175px;top:834px;width:310px;font-family:"Montserrat",sans-serif;font-size:15px;color:var(--teal);line-height:20px}
.post-meta{left:175px;top:886px;font-size:12px;color:#2f3b3f}
.post-meta em{font-style:normal;color:var(--teal)}
.post-text{left:175px;top:904px;width:300px;font-size:10px;line-height:18px;color:#45535a}
.read-btn{left:175px;top:965px;width:251px;height:30px;background:var(--btn-grey);color:var(--white);font-family:"Montserrat",sans-serif;font-weight:700;font-size:10.5px;line-height:30px;padding-left:13px}
.read-btn svg{position:absolute;right:20px;top:11px}
.pop-head{left:502px;top:770px;width:188px}
.pop-item{left:504px;width:188px;height:70px;border-bottom:1px solid #dfe3e4}
.pop-item p{font-size:10px;line-height:17px;color:var(--teal);padding-top:6px}
.pop-item span{display:block;margin-top:4px;font-family:"Montserrat",sans-serif;font-weight:700;font-size:11px;color:var(--teal)}
.feat-head{left:707px;top:770px;width:161px}
.feat-item{left:707px;width:161px;height:68px;border-bottom:1px solid #dfe3e4}
.feat-item h4{font-weight:400;font-size:12px;color:var(--teal);padding-top:4px}
.feat-item p{font-size:10px;line-height:15px;color:#45535a}

/* footer */
.footer{left:0;top:1034px;width:984px;height:128px;background:var(--teal)}
.top-tab{left:809px;top:1012px;width:50px;height:50px;border-radius:50%;background:var(--teal);border:2px solid var(--white)}
.top-tab span{position:absolute;left:0;top:8px;width:100%;text-align:center;color:var(--white);font-family:"Montserrat",sans-serif;font-weight:700;font-size:9px}
.foot-nav{left:118px;top:1069px;font-size:10px;color:#a8c0c5;letter-spacing:.3px}
.foot-nav span{padding:0 9px}
.foot-nav span:first-child{padding-left:0}
.foot-rule{left:118px;top:1091px;width:474px;height:1px;background:#2c6874}
.contact{top:1111px;display:flex;align-items:center;gap:9px;font-size:10px;color:#a8c0c5}
.c-icon{width:16px;height:16px;border-radius:50%;background:#a8c0c5;position:relative}
.stay{left:644px;top:1069px;font-size:10px;color:#a8c0c5}
.stay-rule{left:644px;top:1091px;width:222px;height:1px;background:#2c6874}
.social{display:flex;align-items:center;gap:7px;font-size:10px;color:#a8c0c5}
.social i{display:block;width:15px;height:15px;border-radius:50%;background:#a8c0c5}
.bottom-bar{left:0;top:1162px;width:984px;height:38px;background:var(--teal-deep)}
.copy{left:118px;top:1176px;font-size:9px;color:#8ea9ae}
.copy b{color:var(--white);font-weight:400}
</style>
</head>
<body>
<div class="page">

  <!-- header -->
  <div class="abs top-line"></div>
  <nav class="abs util-nav"><span>ACCUEIL</span><span>PLAN DU SITE</span><span>CODE D'ÉTIQUE</span><span>CONTACT</span><span>ENGLISH</span></nav>
  <div class="abs main-bar"></div>
  <div class="abs logo-box">
    <div class="logo-mark"></div>
    <div class="logo-name">VAROLINQ</div>
    <div class="logo-tag">Recherche de cadres</div>
  </div>
  <nav class="abs main-nav">
    <a class="active">ACCUEIL</a><a>VAROLINQ</a><a>ÉQUIPE</a><a>APPROCHE</a><a>POSTES DISPONIBLES</a><a style="border-right:none">PUBLICATIONS</a>
  </nav>

  <!-- hero -->
  <section class="abs hero">
    <div class="abs hero-photo" role="img" aria-label="Photo d'une personne traçant un réseau de profils de cadres reliés entre eux"></div>
    <div class="abs slide-arrow" style="left:12px"><svg width="10" height="16"><path d="M8 1 L2 8 L8 15" stroke="#fff" stroke-width="3" fill="none"/></svg></div>
    <div class="abs slide-arrow" style="left:932px"><svg width="10" height="16"><path d="M2 1 L8 8 L2 15" stroke="#fff" stroke-width="3" fill="none"/></svg></div>
    <h1 class="abs heading hero-title">LA DIRECTION DE L’AVENIR<br>DE L’AVENIR L’AVENIR</h1>
    <p class="abs hero-text">Varolinq est l’une des firmes de recherche de cadres les plus importantes et les plus aguerries au pays. Depuis notre fondation en 1995, notre équipe de plus de 20 personnes a mené à terme au-delà de 200 mandats par année.</p>
    <div class="abs hero-btn">QUICK APPROACH<svg width="10" height="16"><path d="M2 1 L8 8 L2 15" stroke="#e8a51b" stroke-width="3" fill="none"/></svg></div>
  </section>

  <!-- careers -->
  <section class="abs careers">
    <h2 class="abs heading careers-title">CAREERS &amp; OPPORTUNITIES</h2>
    <div class="abs careers-rule"></div>
    <svg class="abs careers-notch" width="14" height="8"><path d="M0 0 L7 7 L14 0" fill="#8fa3a9"/></svg>

    <div class="abs career" style="left:116px">
      <div class="career-icon"><svg width="20" height="22"><circle cx="10" cy="6" r="5" fill="#0d4a55"/><path d="M0 22 Q0 12 10 12 Q20 12 20 22Z" fill="#0d4a55"/></svg></div>
      <h3 class="heading">LA DIRECTION DE&nbsp; A</h3>
      <p>Varolinq est l’une des firmes de recherche de cadres les plus importantes et les plus</p>
      <div class="apply-btn">APPLY NOW!<svg width="6" height="9"><path d="M0 0 L6 4.5 L0 9Z" fill="#fff"/></svg></div>
    </div>
    <div class="abs career" style="left:377px">
      <div class="career-icon"><svg width="20" height="22"><circle cx="10" cy="6" r="5" fill="#0d4a55"/><path d="M0 22 Q0 12 10 12 Q20 12 20 22Z" fill="#0d4a55"/></svg></div>
      <h3 class="heading">LA DIRECTION DE&nbsp; A</h3>
      <p>Varolinq est l’une des firmes de recherche de cadres les plus importantes et les plus</p>
      <div class="apply-btn">APPLY NOW!<svg width="6" height="9"><path d="M0 0 L6 4.5 L0 9Z" fill="#fff"/></svg></div>
    </div>
    <div class="abs career" style="left:638px">
      <div class="career-icon"><svg width="20" height="22"><circle cx="10" cy="6" r="5" fill="#0d4a55"/><path d="M0 22 Q0 12 10 12 Q20 12 20 22Z" fill="#0d4a55"/></svg></div>
      <h3 class="heading">LA DIRECTION DE&nbsp; A</h3>
      <p>Varolinq est l’une des firmes de recherche de cadres les plus importantes et les plus</p>
      <div class="apply-btn">APPLY NOW!<svg width="6" height="9"><path d="M0 0 L6 4.5 L0 9Z" fill="#fff"/></svg></div>
    </div>
  </section>

  <!-- quick approach form -->
  <form class="abs quick">
    <div class="abs quick-label">QUICK APPROACH</div>
    <svg class="abs quick-arrow" width="22" height="75"><path d="M0 0 L20 37 L0 75" stroke="#1b6472" stroke-width="2" fill="none"/></svg>
    <div class="abs field f-name">Enter Your Name</div>
    <div class="abs field f-mail">E-mail Address</div>
    <div class="abs field f-msg">Message</div>
    <div class="abs submit">SUBMIT</div>
  </form>

  <!-- blog -->
  <h2 class="abs heading col-head blog-head">LATEST BLOG ARTICLES</h2>
  <div class="abs date"><b>20</b><span class="date-month">AUG</span></div>
  <h3 class="abs post-title">WHAT IS VAROLINQ</h3>
  <p class="abs post-sub">IT IS A LONG ESTABLISHED FACT THAT A READER WILL BE</p>
  <p class="abs post-meta">Posted : 1 day ago by - <em>Maribel</em></p>
  <p class="abs post-text">It is a long established fact that a reader will be distracted by the readable content of a page when looking at its layout. The point of using Lorem Ipsum is that it has</p>
  <div class="abs read-btn">READ ALL LATEST BLOG ARTICLES<svg width="6" height="9"><path d="M0 0 L6 4.5 L0 9Z" fill="#fff"/></svg></div>

  <h2 class="abs heading col-head pop-head">POPULAR POSTS</h2>
  <div class="abs pop-item" style="top:803px"><p>Step-By-Step Building Your Own<br>carrers &amp; Opportunities</p><span>LEARN MORE ▸</span></div>
  <div class="abs pop-item" style="top:874px"><p>Step-By-Step Building Your Own<br>carrers &amp; Opportunities</p><span>LEARN MORE ▸</span></div>
  <div class="abs pop-item" style="top:945px;border-bottom:none"><p>Step-By-Step Building Your Own<br>carrers &amp; Opportunities</p><span>LEARN MORE ▸</span></div>

  <h2 class="abs heading col-head feat-head">FEATURED POSTS</h2>
  <div class="abs feat-item" style="top:805px"><h4>It is a long established</h4><p>It is a long established fact that a reader</p></div>
  <div class="abs feat-item" style="top:878px"><h4>It is a long established</h4><p>It is a long established fact that a reader</p></div>
  <div class="abs feat-item" style="top:946px;border-bottom:none"><h4>It is a long established</h4><p>It is a long established fact that a reader</p></div>

  <!-- footer -->
  <footer class="abs footer"></footer>
  <div class="abs top-tab"><span>TOP</span></div>
  <nav class="abs foot-nav"><span>ACCUEIL</span>|<span>VAROLINQ</span>|<span>ÉQUIPE</span>|<span>APPROCHE</span>|<span>POSTES DISPONIBLES</span>|<span>PUBLICATIONS</span></nav>
  <div class="abs foot-rule"></div>
  <div class="abs contact" style="left:118px"><i class="c-icon"></i>+32 2 555 01 27</div>
  <div class="abs contact" style="left:240px"><i class="c-icon"></i>+32 2 555 01 48</div>
  <div class="abs contact" style="left:364px"><i class="c-icon"></i>info@varolinqmail</div>
  <div class="abs stay">STAY CONNECT</div>
  <div class="abs stay-rule"></div>
  <div class="abs social" style="left:648px;top:1108px"><i></i>Chatterly</div>
  <div class="abs social" style="left:726px;top:1108px"><i></i>Birdline</div>
  <div class="abs social" style="left:790px;top:1108px"><i></i>Circlehub</div>
  <div class="abs social" style="left:648px;top:1132px"><i></i>Pinboardy</div>
  <div class="abs social" style="left:726px;top:1132px"><i></i>Worklinked</div>
  <div class="abs bottom-bar"></div>
  <p class="abs copy">Copyright © 2013, <b>VAROLINQ</b> . All Rights Reserved.</p>

</div>
</body>
</html>
```